Corrow Family Farm fresh honey jar label

I need a label for jars of honey harvested at our farm. These are for gifts and personal use. We are looking to incorporate our farm brand into the label. We would like the design to take the existing brand and add some element like bees, honey, flowers, or hives to indicate the contents. We want the design to feel homemade and authentic without feeling cheap or hoaky

Requirements
Must have
• The label must be made to fit a 1" x2" rectangular label. The label must include the attached family brand. The label must include the text "Corrow Family Farms" "Pinebrook, USA" "Farm Fresh Honey". The label will be printed on off-white paper
Nice to have
• It would be nice to have illustrations of bees or flowers around the logo or hives or honeycombs. The label should have a vintage feel
Should not have
• The label should not feel overly cartoonish or hoaky

```html
<!DOCTYPE html>
<html lang="en">
<head>
<meta charset="utf-8">
<title>Corrow Family Farms — Farm Fresh Honey Label</title>
<link href="https://fonts.googleapis.com/css2?family=Cinzel:wght@400;600;700&family=Montserrat:wght@500&display=swap" rel="stylesheet">
<style>
  :root {
    --page: #ffffff;
    --paper: #ebe7db;
    --ink: #3a3331;
    --band: #322c2a;
    --band-text: #e6e1d4;
    --sage: #a9bb98;
    --sage-soft: rgba(169, 187, 152, 0.35);
  }
  * { margin: 0; padding: 0; box-sizing: border-box; }
  html, body {
    width: 1200px; height: 1200px; overflow: hidden;
    background: var(--page);
  }
  .canvas {
    position: relative; width: 1200px; height: 1200px;
  }
  .label {
    position: absolute; left: 65px; top: 162px;
    width: 1070px; height: 875px;
    background: var(--paper);
    box-shadow: 0 2px 10px rgba(0,0,0,0.08);
    overflow: hidden;
    color: var(--ink);
    font-family: "Cinzel", serif;
  }
  .brand {
    position: absolute; left: 0; right: 0; top: 40px;
    display: flex; flex-direction: column; align-items: center;
  }
  .brand-dot {
    width: 64px; height: 64px; border-radius: 50%;
    background: var(--sage);
    margin-bottom: 18px;
  }
  .brand-name {
    font-family: "Montserrat", sans-serif; font-weight: 500;
    font-size: 24px; letter-spacing: 4px; text-transform: uppercase;
    color: var(--ink);
  }
  .brand-place {
    font-family: "Montserrat", sans-serif; font-weight: 500;
    font-size: 17px; letter-spacing: 4px; text-transform: uppercase;
    color: var(--ink); margin-top: 10px;
  }
  .bee-art {
    position: absolute; left: 368px; top: 338px;
    width: 345px; height: 265px;
    border-radius: 50% 50% 45% 45%;
    background: radial-gradient(ellipse at center, var(--sage-soft) 0%, rgba(169,187,152,0.12) 55%, rgba(169,187,152,0) 75%);
  }
  .title {
    position: absolute; left: 0; right: 0; top: 372px;
    text-align: center;
    font-weight: 700; font-size: 70px; letter-spacing: 2px;
    color: var(--ink);
  }
  .nectar {
    position: absolute; left: 0; right: 0; top: 620px;
    text-align: center;
    font-weight: 600; font-size: 23px; line-height: 29px; letter-spacing: 1px;
    color: var(--ink);
  }
  .footer-band {
    position: absolute; left: 0; right: 0; top: 718px; height: 157px;
  }
  .footer-band svg { position: absolute; inset: 0; width: 100%; height: 100%; }
  .tagline {
    position: absolute; left: 0; right: 0; top: 80px;
    text-align: center;
    font-weight: 400; font-size: 24px; letter-spacing: 2px;
    color: var(--band-text); text-transform: uppercase;
  }
</style>
</head>
<body>
<div class="canvas">
  <section class="label">
    <header class="brand">
      <div class="brand-dot"></div>
      <div class="brand-name">Corrow Family Farms</div>
      <div class="brand-place">Pinebrook, USA</div>
    </header>

    <div class="bee-art" role="img" aria-label="Faint vintage engraving of a honey bee framed by a leafy laurel sprig"></div>

    <h1 class="title">Farm Fresh Honey</h1>

    <p class="nectar">
      Organically Cultivated Raw Honey<br>
      With Nectar From Lavender, Catmint, Tulips,<br>
      Hyacinths, Roses, Clematis &amp; Wisteria
    </p>

    <div class="footer-band">
      <svg viewBox="0 0 1070 157" preserveAspectRatio="none" aria-hidden="true">
        <polygon fill="var(--band)" points="0,10 40,6 80,12 120,5 165,11 210,4 255,10 300,6 345,12 390,5 435,9 480,4 525,11 570,6 615,12 660,5 705,10 750,4 795,11 840,6 885,12 930,5 975,10 1020,6 1070,11 1070,157 0,157"/>
      </svg>
      <div class="tagline">Raw honey, harvested from our bee garden</div>
    </div>
  </section>
</div>
</body>
</html>
```